Business Card for a Jewellery Brand

Business card for an upscale jewellery brand. Attached is the brand logo and icon and color board. I am looking for two card versions: one for the founder and one is generic. The card should be elegant and convey upscale and premium feel. I am open to both square and rectangle card shapes.

Industry/Entity Type

Jewelry

Contact Information for Business Card

Two cards: (1) Sunila Perumbadi (Founder) (2) General
(1) Sunila Perumbadi card should have Name: Sunila Perumbadi, Title: Founder Email id: sunila@quelm.com.au. Phone no: +61412555307
(2) Generic card should have Email id: info@quelm.com.au. Phone no: +61431555962

Requirements
Must have
• Workmark
• ICON
• Phone no
• Email ID
• ABN: 48917205563 (Note: ABN is Business number in Australia)
• Website: www.quelm.com.au
• Instagram: quelm_jewellery
• Facebook: @quelmjewellery
Nice to have
• Tagline

```html
<!DOCTYPE html>
<html lang="en">
<head>
<meta charset="utf-8">
<title>QUELM Business Cards</title>
<link rel="stylesheet" href="https://fonts.googleapis.com/css2?family=Raleway:wght@400;500;600&display=swap">
<style>
  :root {
    --page: #ffffff;
    --card: #fce8e2;
    --rose: #e0938d;
    --rose-band: #e9b2b0;
    --marble: #e7dde1;
    --marble-deep: #ddd2d7;
    --grey: #9b9898;
    --shadow: rgba(0, 0, 0, 0.14);
  }
  * { margin: 0; padding: 0; box-sizing: border-box; }
  html, body {
    width: 1200px;
    height: 738px;
    overflow: hidden;
    background: var(--page);
    font-family: "Raleway", sans-serif;
  }
  .canvas {
    position: relative;
    width: 1200px;
    height: 738px;
  }
  .card {
    position: absolute;
    top: 137px;
    width: 464px;
    height: 464px;
    background: var(--card);
    box-shadow: 8px 8px 14px var(--shadow);
    overflow: hidden;
  }
  .card--social { left: 93px; }
  .card--founder { left: 643px; }

  /* Social side */
  .stone-panel {
    position: absolute;
    left: 0; top: 0;
    width: 100%;
    height: 316px;
    background: linear-gradient(135deg, var(--marble) 0%, var(--marble-deep) 55%, var(--marble) 100%);
  }
  .brand-name-mark {
    position: absolute;
    left: 0; top: 128px;
    width: 100%;
    text-align: center;
    font-size: 54px;
    font-weight: 500;
    letter-spacing: 14px;
    padding-left: 14px;
    color: var(--rose);
  }
  .accent-band {
    position: absolute;
    left: 0; top: 316px;
    width: 100%;
    height: 24px;
    background: var(--rose-band);
  }
  .social-list {
    position: absolute;
    left: 121px;
    top: 358px;
    list-style: none;
  }
  .social-item {
    display: flex;
    align-items: center;
    height: 34px;
    margin-bottom: 13px;
    font-size: 25px;
    color: var(--rose);
  }
  .social-item svg { margin-right: 12px; flex: none; }

  /* Founder side */
  .wordmark {
    position: absolute;
    left: 0; top: 84px;
    width: 100%;
    text-align: center;
    font-size: 86px;
    font-weight: 500;
    line-height: 1;
    letter-spacing: 22px;
    padding-left: 22px;
    color: var(--rose);
  }
  .person-name {
    position: absolute;
    left: 0; top: 215px;
    width: 100%;
    text-align: center;
    font-size: 26px;
    font-weight: 600;
    color: var(--rose);
  }
  .person-role {
    position: absolute;
    left: 0; top: 243px;
    width: 100%;
    text-align: center;
    font-size: 19px;
    color: var(--grey);
  }
  .divider {
    position: absolute;
    left: 146px; top: 292px;
    width: 172px;
    height: 1.5px;
    background: var(--rose);
  }
  .contact-list {
    position: absolute;
    left: 0; top: 318px;
    width: 100%;
    list-style: none;
    text-align: center;
    color: var(--grey);
  }
  .contact-list li { font-size: 19px; line-height: 26px; }
  .contact-list .abn { font-size: 15px; line-height: 24px; }
</style>
</head>
<body>
<main class="canvas">
  <section class="card card--social" aria-label="Card back with social handles">
    <div class="stone-panel" role="img" aria-label="Pale pink-grey veined marble texture"></div>
    <div class="brand-name-mark">QUELM</div>
    <div class="accent-band"></div>
    <ul class="social-list">
      <li class="social-item">
        <svg width="34" height="34" viewBox="0 0 34 34" aria-hidden="true"><rect x="2" y="2" width="30" height="30" rx="7" fill="none" stroke="var(--rose)" stroke-width="3"/></svg>
        quelm_jewellery
      </li>
      <li class="social-item">
        <svg width="34" height="34" viewBox="0 0 34 34" aria-hidden="true"><rect x="1" y="1" width="32" height="32" fill="var(--rose)"/></svg>
        @quelmjewellery
      </li>
    </ul>
  </section>

  <section class="card card--founder" aria-label="Founder card front">
    <div class="wordmark">QUELM</div>
    <div class="person-name">Sunila Perumbadi</div>
    <div class="person-role">Founder</div>
    <div class="divider"></div>
    <ul class="contact-list">
      <li>+61412555307</li>
      <li>sunila@quelm.com.au</li>
      <li>www.quelm.com.au</li>
      <li class="abn">ABN: 48917205563</li>
    </ul>
  </section>
</main>
</body>
</html>
```